Quiet Ledger needs a book cover

Enabling people to find a new way of looking at money. If peoples thoughts, attitude and emotions around money are not inline with their goals and dreams then it is often harder to achieve their version of success.

Recognition that we have an emotional and a practical way with money.

Quiet Ledger enables people to find a sustainable (balanced) way with money for their life right now and their future.

Developing this over the years and seeing clients achieve a clear picture/idea/thought connection that is positive around money and it's purpose to them in their lives has truly been fabulous as they have then gone on to achieve their goals and dreams.

Title of book = Quiet Ledger
Tag line = Being healthy being wealthy
Authors Name = Ruth Pell
Book Size = 135 width x 185 height
Thumbnail = Cover must work well as well as full size
Looking for simple and clear app-able / icon type image
Feel free to have fun with it
A simple yet refreshing balanced, eye-catching design.

The back will include authors photo, blurb, testimonials, barcode, ISBN number & price. I will provide once front cover is sorted.

Reason: Realised that the tag line for the book was incorrect.

Target Market(s)

Individuals

Industry/Entity Type

Work

Requirements
Must have
• First work on front cover, once approved we can then do spine and back cover

```html
<!DOCTYPE html>
<html lang="en">
<head>
<meta charset="utf-8">
<title>Quiet Ledger – Book Cover</title>
<link rel="stylesheet" href="https://fonts.googleapis.com/css2?family=Encode+Sans+Condensed:wght@300;800&family=Cinzel:wght@600;700&display=swap">
<style>
  :root {
    --backdrop: #bbbcbe;
    --magenta: #e20a7a;
    --leaf-green: #8cc63f;
    --paper: #ffffff;
    --ink: #111111;
    --note-dark: #9aa193;
    --note-light: #e6e9e1;
  }
  html, body {
    margin: 0;
    padding: 0;
    width: 1200px;
    height: 1192px;
    overflow: hidden;
    background: var(--backdrop);
  }
  .canvas {
    position: relative;
    width: 1200px;
    height: 1192px;
  }
  .cover {
    position: absolute;
    left: 245px;
    top: 56px;
    width: 710px;
    height: 1068px;
    background: var(--paper);
    overflow: hidden;
  }
  .title-band {
    position: absolute;
    left: 0;
    top: 0;
    width: 710px;
    height: 250px;
    background: var(--magenta);
  }
  .title-svg {
    position: absolute;
    left: 0;
    top: 0;
    width: 710px;
    height: 420px;
  }
  .title-top {
    font-family: "Encode Sans Condensed", sans-serif;
    font-weight: 300;
    fill: var(--paper);
  }
  .title-bottom {
    font-family: "Encode Sans Condensed", sans-serif;
    font-weight: 800;
    fill: var(--leaf-green);
  }
  .tagline {
    position: absolute;
    left: 0;
    top: 446px;
    width: 710px;
    margin: 0;
    text-align: center;
    font-family: "Cinzel", serif;
    font-weight: 700;
    font-size: 40px;
    line-height: 52px;
    text-transform: uppercase;
    color: var(--ink);
  }
  .cover-image {
    position: absolute;
    left: 260px;
    top: 635px;
    width: 190px;
    height: 300px;
    background: linear-gradient(180deg, var(--note-light) 0%, var(--note-dark) 100%);
  }
  .author-band {
    position: absolute;
    left: 0;
    bottom: 0;
    width: 710px;
    height: 88px;
    background: var(--magenta);
    display: flex;
    align-items: center;
    justify-content: center;
  }
  .author {
    margin: 0;
    font-family: "Cinzel", serif;
    font-weight: 600;
    font-size: 46px;
    letter-spacing: 0.2em;
    padding-left: 0.2em;
    color: var(--paper);
  }
</style>
</head>
<body>
<div class="canvas">
  <main class="cover">
    <div class="title-band"></div>
    <svg class="title-svg" viewBox="0 0 710 420" aria-label="Quiet Ledger">
      <text class="title-top" x="68" y="218" font-size="186" textLength="610" lengthAdjust="spacingAndGlyphs">QUIET</text>
      <text class="title-bottom" x="70" y="412" font-size="196" textLength="606" lengthAdjust="spacingAndGlyphs">LEDGER</text>
    </svg>
    <p class="tagline">Being healthy<br>being wealthy</p>
    <div class="cover-image" role="img" aria-label="Photo of rolled banknotes tied with a ribbon"></div>
    <footer class="author-band">
      <p class="author">RUTH PELL</p>
    </footer>
  </main>
</div>
</body>
</html>
```